Soziale Betreuung für Senioren, die von Herzen kommt!
Zielgruppe
Betreuung von Senioren (keine Pflege) mit den 3 Schwerpunkten „Miteinander reden“, „im Alltag unterstützen“ und „Freizeit gestalten“
Aufgabenstellung
Entwicklung eines Flyers als Hauptwerbemedium, das Interesse bei den Senioren weckt (große
Buchstaben für den Teil, der sich an die Senioren richtet) und auch die Angehörigen überzeugt.
DIN A4 Lang 6-seitig Wickelfalz.

```html
<!DOCTYPE html>
<html lang="de">
<head>
<meta charset="utf-8">
<title>Soziale Betreuung für Senioren – Flyer</title>
<link rel="stylesheet" href="https://fonts.googleapis.com/css2?family=Tinos:ital,wght@0,400;0,700;1,400&display=swap">
<style>
:root{
  --stage:#8e8f92;
  --paper:#f8e9c6;
  --red:#d6161c;
  --ink:#1f1a17;
  --photo-grey:#c9c9cb;
  --photo-skin:#b88a6e;
  --photo-warm:#8a6a4c;
  --photo-green:#4f6d45;
  --font:"Tinos","Times New Roman",serif;
}
*{box-sizing:border-box;margin:0;padding:0}
html,body{width:1200px;height:800px;overflow:hidden}
body{background:var(--stage);font-family:var(--font);color:var(--ink);position:relative}
.sheet{position:absolute;top:195px;width:580px;height:410px;background:var(--paper);display:flex;box-shadow:0 6px 18px rgba(0,0,0,.25)}
.sheet--outside{left:15px}
.sheet--inside{left:605px}
.panel{position:relative;width:33.333%;height:100%;overflow:hidden;border-right:1px solid rgba(0,0,0,.08)}
.panel:last-child{border-right:none}
.photo{position:absolute}
.heading{font-size:15px;letter-spacing:1.5px;font-weight:700;display:inline-block;border-bottom:2px solid var(--red);padding-bottom:1px;line-height:1.1}
.copy{font-size:6.6px;letter-spacing:.4px;line-height:1.45}
.accent{color:var(--red)}
.tick{width:14px;height:12px;flex:none}
/* Outside: offer */
.offer .photo{left:12px;top:0;width:170px;height:150px;background:linear-gradient(160deg,#9aa0a6,#6d7580 60%,#8a94a0)}
.offer .body{position:absolute;top:160px;left:14px;right:12px}
.offer .lead{font-size:7px;font-weight:700;font-style:italic;margin:5px 0 6px}
.offer .copy p{margin-bottom:6px}
.signature{width:70px;height:14px;background:rgba(31,26,23,.15);margin-top:4px}
/* Outside: contact */
.contact .figure{position:absolute;left:36px;top:26px;width:122px;height:130px;background:linear-gradient(180deg,#e02a2e,#c11217);border-radius:40% 40% 8px 8px}
.contact .heading{position:absolute;top:180px;left:50%;transform:translateX(-50%);font-size:19px}
.contact-list{position:absolute;top:222px;left:14px;right:8px;list-style:none;font-size:8px;letter-spacing:.8px;line-height:1.3}
.contact-list li{display:flex;gap:8px;align-items:flex-start;margin-bottom:10px}
.contact-list svg{width:14px;height:14px;flex:none;stroke:var(--red);fill:none;stroke-width:1.4}
/* Outside: cover */
.cover{border-top:4px solid var(--red);border-bottom:4px solid var(--red)}
.cover .title{position:absolute;top:14px;left:12px;right:10px;font-size:17px;letter-spacing:2px;line-height:1.15}
.cover .sub{display:block;text-align:right;font-size:10px;letter-spacing:1.5px}
.cover .heart-line{display:flex;justify-content:space-between;align-items:flex-end;font-size:11px;letter-spacing:1.5px;margin-top:4px}
.cover .heart{width:34px;height:30px;fill:var(--red)}
.cover .photo{left:0;top:112px;width:100%;height:150px;background:linear-gradient(120deg,var(--photo-skin),#d8b39a 45%,var(--photo-grey));border-top:3px solid var(--red);border-bottom:3px solid var(--red);border-radius:0 0 0 40% / 0 0 0 20%}
.checklist{position:absolute;top:276px;left:12px;right:6px;list-style:none;font-size:12px;letter-spacing:1.3px}
.checklist li{display:flex;gap:6px;align-items:center;margin-bottom:6px}
.brand{position:absolute;right:10px;bottom:10px;display:flex;align-items:center;gap:4px;font-size:9px;letter-spacing:.8px;color:var(--red)}
.brand::before{content:"";width:9px;height:9px;border-radius:50%;background:var(--red)}
/* Inside */
.inside-panel{padding:12px 12px}
.inside-panel .heading{font-size:12px;margin-bottom:5px}
.subhead{color:var(--red);font-weight:700;font-size:7px;letter-spacing:.6px;margin-top:7px}
.section-head{display:flex;align-items:flex-end;gap:4px;margin-bottom:4px}
.section-head .heading{margin-bottom:0}
.inside-panel .photo{position:relative;height:62px;margin:5px 0}
.photo--park{background:linear-gradient(135deg,#b5652b,#d9a45c 40%,#3a4260)}
.photo--rabbit{background:linear-gradient(135deg,#3b4a8a,#c9c3bd 50%,#c0302f)}
.photo--trees{background:linear-gradient(135deg,var(--photo-green),#8fae7a 50%,#b79a6c)}
.costs{margin-top:6px}
.inside-panel .brand{right:12px;bottom:10px}
</style>
</head>
<body>

<section class="sheet sheet--outside" aria-label="Flyer Außenseite">
  <article class="panel offer">
    <div class="photo" role="img" aria-label="Porträtfoto der Betreuerin"></div>
    <div class="body">
      <h2 class="heading">Mein Angebot</h2>
      <p class="lead">Was ist eigentlich soziale Betreuung?</p>
      <div class="copy">
        <p>Lieber Interessent,</p>
        <p>es freut mich, dass Sie sich Zeit für dieses Informationsblatt nehmen.</p>
        <p>In meiner Dienstleistung geht es um „soziale Betreuung“, die dazu beitragen soll, den Alltag zu strukturieren, zu begleiten und mehr Lebensfreude zu gewinnen.</p>
        <p>Ich, Helga Marwitz, möchte Ihnen in dieser Informationsschrift mehr darüber erzählen.</p>
        <p>Es grüßt Sie herzlich Ihre</p>
      </div>
      <div class="signature" role="img" aria-label="Handschriftliche Unterschrift H. Marwitz"></div>
    </div>
  </article>

  <article class="panel contact">
    <div class="figure" role="img" aria-label="Rote Illustration eines älteren Paares mit Gehstock"></div>
    <h2 class="heading">Kontakt</h2>
    <ul class="contact-list">
      <li><svg viewBox="0 0 16 16"><rect x="1.5" y="3.5" width="13" height="9"/><path d="M1.5 3.5l6.5 5 6.5-5"/></svg><span>Helga Marwitz<br>Lindenweg 12<br>48151 Musterstadt</span></li>
      <li><svg viewBox="0 0 16 16"><path d="M4 2l3 3-2 2c1 2 2 3 4 4l2-2 3 3-2 2C7 14 2 9 2 4z"/></svg><span>0211 / 45 67 89</span></li>
      <li><svg viewBox="0 0 16 16"><rect x="5" y="1.5" width="6" height="13" rx="1"/><path d="M6.5 4h3M7 12h2"/></svg><span>0171 / 23 45 67 89</span></li>
      <li><svg viewBox="0 0 16 16"><circle cx="8" cy="8" r="2.5"/><path d="M10.5 8v1.5a2 2 0 0 0 4 0V8a6.5 6.5 0 1 0-3 5.5"/></svg><span>info@herzenszeit-betreuung.de</span></li>
      <li><svg viewBox="0 0 16 16"><circle cx="8" cy="8" r="6.5"/><ellipse cx="8" cy="8" rx="3" ry="6.5"/><path d="M1.5 8h13M2.5 5h11M2.5 11h11"/></svg><span>www.herzenszeit-betreuung.de</span></li>
    </ul>
  </article>

  <article class="panel cover">
    <h1 class="title">Soziale Betreuung
      <span class="sub">für Senioren,</span>
      <span class="heart-line"><span>die von</span>
        <svg class="heart" viewBox="0 0 32 28" aria-label="Herz" role="img"><path d="M16 27C6 19 1 14 1 8a7 7 0 0 1 15-3 7 7 0 0 1 15 3c0 6-5 11-15 19z"/></svg>
        <span>kommt!</span></span>
    </h1>
    <div class="photo" role="img" aria-label="Foto: junge Hand hält die Hand einer Seniorin"></div>
    <ul class="checklist">
      <li><svg class="tick" viewBox="0 0 14 12"><path d="M1 6l4 5L13 1" fill="none" stroke="#d6161c" stroke-width="2"/></svg>Miteinander reden</li>
      <li><svg class="tick" viewBox="0 0 14 12"><path d="M1 6l4 5L13 1" fill="none" stroke="#d6161c" stroke-width="2"/></svg>Im Alltag unterstützen</li>
      <li><svg class="tick" viewBox="0 0 14 12"><path d="M1 6l4 5L13 1" fill="none" stroke="#d6161c" stroke-width="2"/></svg>Freizeit gestalten</li>
    </ul>
    <div class="brand">Herzenszeit</div>
  </article>
</section>

<section class="sheet sheet--inside" aria-label="Flyer Innenseite">
  <article class="panel inside-panel">
    <h2 class="heading">Infos für die Angehörigen</h2>
    <div class="copy">
      <p>Ich möchte Sie gern überzeugen, dass meine Hilfe von Senioren dankbar angenommen wird.</p>
      <p class="subhead">Weniger Stress für alle</p>
      <p>Als Angehöriger ist man oft vor besondere Herausforderungen gestellt. Schon ein plötzlich notwendiger Arztbesuch der Eltern/Großeltern bringt den Zeitplan ins Wanken.</p>
      <p>-Ich begleite die Senioren zum Arzt, auf Wunsch bis ins Behandlungszimmer!</p>
      <p class="subhead">Mehr Zeit für die schönen Dinge</p>
      <p>In der täglichen Routine gerät man leicht in Streit. Während man selbst unter permanentem Zeitdruck leidet, haben Senioren häufig ein anderes Zeitempfinden.</p>
      <p>-Gewinnen Sie mehr gemeinsame Zeit für die schönen Dinge miteinander!</p>
      <p class="subhead">Unterstützung durch eine weitere Bezugsperson</p>
      <p>Wie empfinden die Senioren die Unterstützung eines Dritten?<br>-Der neue Kontakt mit weiteren Bezugspersonen wird sehr häufig als Bereicherung empfunden.</p>
      <p>Sofern ein Angehöriger an Demenz erkrankt oder erkrankt ist, ist professionelle Hilfe, Unterstützung und Beratung gefragt. -Ich unterstütze Sie gern!</p>
      <p>Ich bin zertifizierte Demenzbegleiterin.</p>
    </div>
  </article>

  <article class="panel inside-panel">
    <div class="section-head"><svg class="tick" viewBox="0 0 14 12"><path d="M1 6l4 5L13 1" fill="none" stroke="#d6161c" stroke-width="2"/></svg><h2 class="heading">Miteinander reden</h2></div>
    <div class="copy">
      <p>Zeit für gemeinsame Gespräche ohne Eile, ohne Hektik. Respektvoll mit Vertrauen und Nächstenliebe.</p>
      <p class="accent">Das ist mein Versprechen an Sie!</p>
      <p>Gespräche über das, was Sie bewegt, oder einfach über Dinge lachen.</p>
    </div>
    <div class="photo photo--park" role="img" aria-label="Foto: Senior und Seniorin im herbstlichen Park"></div>
    <div class="section-head"><svg class="tick" viewBox="0 0 14 12"><path d="M1 6l4 5L13 1" fill="none" stroke="#d6161c" stroke-width="2"/></svg><h2 class="heading">Im Alltag unterstützen</h2></div>
    <div class="copy">
      <p>Ich unterstütze Sie gern darin, den Haushalt zusammen mit Ihnen zu organisieren. Ein schönes Gefühl, vieles noch selbst zu schaffen. Mit ein wenig Unterstützung:</p>
      <p class="accent">Mehr Mobilität und Sicherheit für Sie!</p>
    </div>
    <div class="photo photo--rabbit" role="img" aria-label="Foto: Seniorin betrachtet ein Kaninchen im Stall"></div>
  </article>

  <article class="panel inside-panel">
    <div class="section-head"><svg class="tick" viewBox="0 0 14 12"><path d="M1 6l4 5L13 1" fill="none" stroke="#d6161c" stroke-width="2"/></svg><h2 class="heading">Freizeit gestalten</h2></div>
    <div class="copy">
      <p>Schönes erleben, in einem nicht alltäglichen Umfeld. Eine Auszeit, um neue Kraft zu finden.</p>
      <p class="accent">Sich auf etwas freuen, etwas vorhaben.</p>
      <p>Wenn Sie es wünschen, auch gern bei Ihnen zu Hause.</p>
    </div>
    <div class="photo photo--trees" role="img" aria-label="Foto: zwei Seniorinnen im Grünen auf einer Bank"></div>
    <div class="costs">
      <h2 class="heading">Kosten:</h2>
      <div class="copy">
        <p>Ich arbeite allein und ohne administrative Verwaltung oder repräsentative Geschäftsräume. Diesen Kostenvorteil gebe ich an Sie weiter. Auch der Einsatz meines PKWs erfolgt im aller Regel ohne gesonderte Berechnung. Kann in vielen Fällen über die Pflegeversicherung abgerechnet werden.</p>
        <p class="accent"><b>Sprechen Sie mich gern unverbindlich an.</b></p>
      </div>
    </div>
    <div class="brand">Herzenszeit</div>
  </article>
</section>

</body>
</html>
```